Business card and stationery
Clear Harbour
Project: Business card and stationery
Business card and stationery  -
Creative Brief
Simple
Name Surname
Executive Director
317 Larkmoor Lane, #03 Fenwick Plaza, Country 264519
vantolemu@mailpost.example
www.clearharbour.example.sg
info (name, address, email etc) on the card should be editable for each employee

```html
<!DOCTYPE html>
<html lang="en">
<head>
<meta charset="utf-8">
<title>Clear Harbour — Business Card</title>
<link href="https://fonts.googleapis.com/css2?family=Open+Sans:wght@400;600;700&display=swap" rel="stylesheet">
<style>
  :root {
    --bg: #ecebe8;
    --card-top: #ffffff;
    --card-bottom: #e4e4e4;
    --brand-blue: #2f6fe0;
    --brand-green: #33b82e;
    --ink: #3a3a3a;
    --ink-soft: #666666;
    --rule: #c9c9c9;
  }
  * { box-sizing: border-box; margin: 0; padding: 0; }
  html, body { width: 1200px; height: 581px; overflow: hidden; }
  body {
    background: var(--bg);
    font-family: "Open Sans", Arial, sans-serif;
    position: relative;
  }
  .card {
    position: absolute;
    top: 137px;
    width: 552px;
    height: 370px;
    border-radius: 14px;
    background: linear-gradient(180deg, var(--card-top) 0%, var(--card-top) 55%, var(--card-bottom) 100%);
    box-shadow: 0 3px 10px rgba(0,0,0,0.25);
    overflow: hidden;
  }
  .card--front { left: 29px; }
  .card--back { left: 612px; }
  .card__swoosh { position: absolute; inset: 0; }
  .brand-name {
    position: absolute;
    color: var(--brand-blue);
    font-weight: 700;
    font-size: 38px;
    letter-spacing: -0.5px;
    white-space: nowrap;
    transform: translateX(-50%);
  }
  .card--front .brand-name { left: 320px; top: 108px; }
  .card--back .brand-name { left: 276px; top: 152px; }
  .identity {
    position: absolute;
    right: 307px;
    top: 222px;
    text-align: right;
  }
  .identity__name { color: var(--brand-blue); font-weight: 700; font-size: 23px; line-height: 1.1; }
  .identity__title { color: var(--ink); font-weight: 700; font-size: 13px; margin-top: 2px; }
  .identity__address { color: var(--ink); font-size: 13px; line-height: 19px; margin-top: 24px; }
  .divider {
    position: absolute;
    left: 259px; top: 232px;
    width: 1px; height: 120px;
    background: var(--rule);
  }
  .contacts { position: absolute; left: 270px; top: 236px; list-style: none; }
  .contacts li {
    display: flex; align-items: center; gap: 8px;
    color: var(--ink); font-size: 12.5px; height: 29px;
  }
  .contacts svg { width: 13px; height: 13px; flex: none; }
  .website {
    position: absolute; left: 0; right: 0; top: 323px;
    text-align: center; color: var(--ink); font-weight: 700; font-size: 15px;
  }
</style>
</head>
<body>

<section class="card card--front">
  <svg class="card__swoosh" viewBox="0 0 552 370" preserveAspectRatio="none" aria-hidden="true">
    <path d="M0 0 H105 C70 70 35 170 0 300 Z" fill="var(--brand-blue)"/>
    <path d="M105 0 H120 C80 80 40 190 0 330 V300 C35 170 70 70 105 0 Z" fill="var(--brand-green)"/>
    <path d="M475 0 H552 V370 H520 C560 250 540 110 475 0 Z" fill="var(--brand-blue)"/>
    <path d="M462 0 H475 C540 110 560 250 520 370 H508 C548 250 528 110 462 0 Z" fill="var(--brand-green)"/>
  </svg>

  <div class="brand-name">Clear Harbour</div>

  <div class="identity">
    <div class="identity__name">Name Surname</div>
    <div class="identity__title">Executive Director</div>
    <div class="identity__address">317 Larkmoor Lane,<br>#03 Fenwick Plaza,<br>Country 264519</div>
  </div>

  <div class="divider"></div>

  <ul class="contacts">
    <li><svg viewBox="0 0 16 16"><path d="M4 1 L6.5 4 L5 6 C6 8.5 7.5 10 10 11 L12 9.5 L15 12 L13 15 C7 14 2 9 1 3 Z" fill="var(--brand-blue)"/></svg>+77 7777 7777</li>
    <li><svg viewBox="0 0 16 16"><rect x="1" y="3" width="14" height="10" rx="2" fill="var(--brand-blue)"/></svg>+88 8888 8888</li>
    <li><svg viewBox="0 0 16 16"><circle cx="8" cy="8" r="7" fill="var(--brand-blue)"/><path d="M4 6 L8 9 L12 6" stroke="#fff" stroke-width="1.4" fill="none"/></svg>vantolemu@mailpost.example</li>
    <li><svg viewBox="0 0 16 16"><circle cx="8" cy="8" r="7" fill="var(--brand-blue)"/><path d="M1.5 8 H14.5 M8 1 C5 5 5 11 8 15 C11 11 11 5 8 1" stroke="#fff" stroke-width="1.1" fill="none"/></svg>www.clearharbour.example.sg</li>
  </ul>
</section>

<section class="card card--back">
  <div class="brand-name">Clear Harbour</div>
  <div class="website">www.clearharbour.example.sg</div>
</section>

</body>
</html>
```